Contemporary new French wine brand needs logo and series of label design

to design a new contemporary logo and series of labels for a new French wine brand. We hope to attract not just current French wine drinkers but new ones who may appreciate a less traditional and more modern style.
Updates

Reason: we are wanting to extend the project for a few days more to receive more submissions since we had fewer designs submitted than we were expecting, maybe because of the holidays.

Target Market(s)

people who follow the arts community (eg. music, theatre, visual/video arts, dance) --- all mature ages.

Industry/Entity Type

French Wine

Requirements
Must have
• a clear, memorable treatment for the name CLAVINE with accompanying logo.
Nice to have
• embossing, matte/gloss refinement, tasteful foil stamping, coated stock for the whites to help the integrity of the paper in and out of ice buckets. A combo of say, three types of fonts; a semi custom font for the brand name Clavine and maybe a script and one other.
Should not have
• not traditional French

```html
<!DOCTYPE html>
<html lang="fr">
<head>
<meta charset="utf-8">
<title>Clavine – Val de Loire labels</title>
<link rel="stylesheet" href="https://fonts.googleapis.com/css2?family=Marcellus&family=Pinyon+Script&display=swap">
<style>
  :root {
    --page: #ffffff;
    --stock: #f7f7f8;
    --stock-edge: #e6e7ea;
    --ink: #1d1b1a;
    --gold: #a8712f;
    --gold-dark: #7d4f1c;
    --gold-light: #e3bb74;
  }
  * { margin: 0; padding: 0; box-sizing: border-box; }
  html, body {
    width: 1200px; height: 1000px; overflow: hidden;
    background: var(--page);
  }
  .label-series {
    width: 1200px; height: 1000px;
    display: flex; align-items: center; justify-content: center; gap: 60px;
  }
  .wine-label {
    position: relative;
    width: 500px; height: 440px;
    background:
      radial-gradient(circle at 30% 20%, #ffffff 0%, var(--stock) 60%, #eeeff2 100%);
    border: 1px solid var(--stock-edge);
    box-shadow: 0 2px 8px rgba(0,0,0,0.12);
    display: flex; flex-direction: column; align-items: center;
    overflow: hidden;
  }
  .brand-mark {
    margin-top: 38px;
    width: 70px; height: 70px;
    border: 2px solid var(--gold);
    border-radius: 50%;
  }
  .brand-name {
    margin-top: 22px;
    font-family: "Marcellus", serif;
    font-size: 42px;
    letter-spacing: 1px;
    color: var(--ink);
    line-height: 1;
  }
  .varietal {
    margin-top: 20px;
    font-family: "Marcellus", serif;
    font-size: 27px;
    letter-spacing: 3px;
    color: var(--gold);
    line-height: 1;
  }
  .varietal-rule {
    margin-top: 14px;
    width: 296px; height: 3px;
    background: linear-gradient(90deg, var(--gold-dark), var(--gold-light) 50%, var(--gold-dark));
  }
  .appellation {
    margin-top: 22px;
    font-family: "Pinyon Script", cursive;
    font-size: 38px;
    color: var(--ink);
    line-height: 1;
  }
  .ornament-band {
    position: absolute; left: 0; right: 0; bottom: 32px;
    height: 36px;
    background: linear-gradient(90deg, var(--gold-dark), var(--gold-light) 30%, var(--gold) 55%, var(--gold-light) 80%, var(--gold-dark));
  }
</style>
</head>
<body>
  <main class="label-series">
    <article class="wine-label">
      <div class="brand-mark" aria-hidden="true"></div>
      <h1 class="brand-name">CLAVINE</h1>
      <p class="varietal">SAUVIGNON BLANC</p>
      <div class="varietal-rule"></div>
      <p class="appellation">Val de Loire</p>
      <div class="ornament-band" role="img" aria-label="Gold foil ornamental border band"></div>
    </article>
    <article class="wine-label">
      <div class="brand-mark" aria-hidden="true"></div>
      <h1 class="brand-name">CLAVINE</h1>
      <p class="varietal">CABERNET FRANC</p>
      <div class="varietal-rule"></div>
      <p class="appellation">Val de Loire</p>
      <div class="ornament-band" role="img" aria-label="Gold foil ornamental border band"></div>
    </article>
  </main>
</body>
</html>
```